Give Tall Oak Ridge an Online Presence!

Tall Oak Ridge Property Maintenance is an Australian Owned property maintenance company who needs a stand out online presence.

TOR maintains many buildings and sites and wants to appeal to a corporate professional market with their brand new website. TOR is essentially a handyman service offering all maintenance services to home owners, office managers, real estate agents and strata managers.

The Website:
We need a corporate website that appeals to our broader customer base (property owners, property managers, office managers) the copy is being written by a professional so use filler text for now.

Things that we want:
Home page that sets us apart and appeals to the corporate and residential market. The home page needs to not focus on either the residential or commercial market. The home page should focus on our logo and branding. We have a logo already and it is attached to the brief, please use it and try to consider the colour pallette that goes with it. Whilst we want the site to appear strong and manly it is important to remember that 95% of our customers are female so we need the site to be appealing to women. Women need to believe that we are strong, dependable and trustworthy.
We'd like a quote page and potentially also the ability to get a quote from the home page (please don't put it in if it ruins the overall feel of the home page)
An "about us" page
A contact us page
A blog that's built in (we don't want to link to an external blog)
(overall we'd expect to have 6 or 7 pages total)

The site will also need coding - we expect this to be done in a separate project but need you to consider a few things about the coding side of things.

It needs to be iPhone and iPad compatible.

We'd like you to suggest the best CMS that you would use or if you would suggest not using a CMS please let us know with your submissions.

Target Market(s)

Property owners, office managers and property managers who need maintenance on buildings (So all of them)

Industry/Entity Type

Property Maintenance

Requirements
Must have
• Our Logo
Home page
About Us
Residential
Commercial
Real Estate/Strata
Contact Us/Quote
Blog
Nice to have
• Quote form included in home page
Movement on the home page at least
Should not have
• other logos, too much colour
NO FLASH

```html
<!DOCTYPE html>
<html lang="en">
<head>
<meta charset="utf-8">
<title>Tall Oak Ridge Property Maintenance</title>
<link href="https://fonts.googleapis.com/css2?family=Source+Sans+3:ital,wght@0,400;0,600;0,700;1,400&family=Baloo+2:wght@700&display=swap" rel="stylesheet">
<style>
:root{
  --orange:#f7921e;
  --orange-dark:#e07b10;
  --heading:#d9781a;
  --charcoal:#2f2f2f;
  --header:#5c5c5c;
  --header-dark:#454545;
  --text:#4a4a4a;
  --muted:#6b6b6b;
  --panel:#f2f2f2;
  --page:#ffffff;
  --top-bg:#f3f3f3;
}
*{margin:0;padding:0;box-sizing:border-box}
html,body{width:1200px;height:1148px;overflow:hidden}
body{position:relative;background:var(--page);font-family:"Source Sans 3",Arial,sans-serif;color:var(--text)}
.abs{position:absolute}

.top-area{left:0;top:0;width:1200px;height:417px;background:linear-gradient(#fafafa,var(--top-bg))}
.site-header{left:0;top:0;width:1200px;height:71px;background:linear-gradient(#666,var(--header-dark));border-bottom:1px solid #bbb}
.brand-tab{left:90px;top:0;width:143px;height:112px;background:linear-gradient(#3a3a3a,#1f1f1f);border-radius:0 0 30px 30px / 0 0 12px 12px;box-shadow:0 3px 4px rgba(0,0,0,.35);display:flex;flex-direction:column;align-items:center;justify-content:center;gap:6px}
.brand-mark{width:18px;height:18px;border-radius:50%;background:var(--orange)}
.brand-name{color:var(--orange);font-weight:700;font-size:13px;text-align:center;line-height:1.1;text-transform:uppercase;width:110px}
.main-nav{left:275px;top:14px;display:flex;align-items:center;height:40px}
.main-nav a{color:#fff;text-decoration:none;font-size:13px;font-weight:600;letter-spacing:.1px;padding:0 21px;line-height:40px;height:40px}
.main-nav a.current{background:var(--orange);color:#5a2a00;border-radius:4px;padding:0 22px;margin-right:8px}
.main-nav a:last-child{padding-right:0}
.contact-line{left:276px;top:88px;font-size:18px;color:#333;word-spacing:1px}
.contact-line .sep{margin:0 30px}

.slider-frame{left:90px;top:125px;width:763px;height:262px;background:#e5e5e5;border-radius:4px;box-shadow:0 6px 8px -6px rgba(0,0,0,.4)}
.slide{left:96px;top:131px;width:751px;height:250px;border-radius:4px;overflow:hidden;background:linear-gradient(90deg,#9d9d9d 0,#a5a5a5 49%,#8b5a3c 50%,#c9b8a0 100%)}
.slide-photo{position:absolute;right:0;top:0;width:376px;height:250px;background:linear-gradient(90deg,#7d4b30,#a67b58 45%,#d8d2c4 100%)}
.slide-title{left:160px;top:196px;font-size:31px;font-weight:400;color:#333;letter-spacing:-.3px}
.btn-more{left:163px;top:247px;width:79px;height:28px;border-radius:14px;background:linear-gradient(#fff,#ddd);box-shadow:0 1px 3px rgba(0,0,0,.4);font-size:12px;color:#555;text-align:center;line-height:28px}
.dots{left:118px;top:350px;display:flex;gap:12px}
.dots span{width:9px;height:9px;border-radius:50%;background:#fff}
.dots span.on{background:#333}

.quote-box{left:863px;top:125px;width:249px;height:262px;background:linear-gradient(#f79a2a,var(--orange-dark));border-radius:4px}
.quote-title{left:875px;top:100px;font-family:"Baloo 2",Arial,sans-serif;font-weight:700;font-size:30px;color:#555;-webkit-text-stroke:1.5px #fff;paint-order:stroke fill;letter-spacing:-.3px}
.quote-form label{position:absolute;left:880px;font-size:12px;color:#3a2000}
.quote-form .field{position:absolute;left:935px;width:165px;height:29px;background:#fff;border:1px solid #c96b0a;box-shadow:inset 0 1px 2px rgba(0,0,0,.2)}
.btn-submit{left:1022px;top:348px;width:78px;height:27px;border-radius:14px;background:linear-gradient(#666,#3c3c3c);color:#fff;font-size:14px;font-style:italic;text-align:center;line-height:27px}

.section-title{color:var(--heading);font-weight:400}
.welcome-title{left:92px;top:444px;font-size:24px}
.body-copy{font-size:12.5px;line-height:23px;text-align:justify;color:var(--text)}
.welcome-copy{left:91px;top:488px;width:764px}
.welcome-photo{left:892px;top:440px;width:203px;height:155px;border-radius:6px;background:radial-gradient(circle at 70% 40%,#e23a26 0,#c8301f 25%,#5a4638 45%,#fff 75%)}
.divider{left:90px;top:628px;width:1022px;border-top:2px dotted #999}

.services-title{left:90px;top:661px;font-size:19px}
.services-rule{left:90px;top:702px;width:764px;height:1px;background:#ccc}
.services-intro{left:91px;top:720px;width:763px}
.service-thumb{left:90px;width:201px;height:113px;border:3px solid #ddd;border-radius:8px}
.thumb-tools{top:787px;background:linear-gradient(135deg,#8a2b1c 0,#c79a6b 20%,#e2c39a 60%,#b98e62 100%)}
.thumb-electric{top:923px;background:linear-gradient(#f3f3f3,#d6d3cc 60%,#b7b0a3 100%)}
.service-copy{left:311px;width:542px}
.service-copy a{color:var(--heading);text-decoration:none}

.other-title{left:885px;top:661px;font-size:19px}
.other-panel{left:882px;top:701px;width:226px;height:335px;background:var(--panel);border-radius:8px}
.other-list{left:906px;top:722px;list-style:none}
.other-list li{font-size:13.5px;color:var(--muted);height:37.5px;display:flex;align-items:center;gap:11px}
.other-list svg{flex:none}

.site-footer{left:0;top:1061px;width:1200px;height:87px;background:#2b2b2b}
.footer-nav{left:92px;top:1080px;font-size:13px;color:#bbb}
.footer-nav a{color:#c8c8c8;text-decoration:none}
.footer-nav .bar{margin:0 8px;color:#888}
.copyright{left:92px;top:1112px;font-size:12.5px;color:#bbb}
.copyright span{margin-left:16px}
.social{left:1048px;top:1092px;display:flex;gap:8px}
.social span{width:29px;height:29px;border-radius:50%;background:#fff}
</style>
</head>
<body>
<div class="abs top-area"></div>

<header class="abs site-header"></header>
<div class="abs brand-tab">
  <span class="brand-mark"></span>
  <span class="brand-name">Tall Oak Ridge</span>
</div>
<nav class="abs main-nav">
  <a class="current" href="#">HOME</a>
  <a href="#">ABOUT US</a>
  <a href="#">RESIDENTIAL</a>
  <a href="#">COMMERCIAL</a>
  <a href="#">REAL ESTATE/STRATA</a>
  <a href="#">CONTACT US/QUOTE</a>
  <a href="#">BLOG</a>
</nav>
<div class="abs contact-line">Call us : 555 010 2481<span class="sep">|</span>E-Mail : info@tallridgemaint.com.au</div>

<div class="abs slider-frame"></div>
<div class="abs slide">
  <div class="slide-photo" role="img" aria-label="Photo of a smiling couple standing at the front door of their brick home"></div>
</div>
<div class="abs slide-title">Duis aute irure dolor</div>
<div class="abs btn-more">View more</div>
<div class="abs dots"><span class="on"></span><span></span><span></span><span></span></div>

<div class="abs quote-box"></div>
<div class="abs quote-title">Get a Quote</div>
<form class="quote-form">
  <label style="top:167px">Name :</label><span class="field" style="top:160px"></span>
  <label style="top:199px">Phone :</label><span class="field" style="top:192px"></span>
  <label style="top:231px">Email :</label><span class="field" style="top:224px"></span>
  <label style="top:263px">Address :</label><span class="field" style="top:256px;height:83px"></span>
</form>
<div class="abs btn-submit">SUBMIT</div>

<h1 class="abs section-title welcome-title">Welcome to our site</h1>
<p class="abs body-copy welcome-copy">Sed ut perspiciatis unde omnis iste natus error sit voluptatem accusantium doloremque laudantium, totam rem aperiam, eaque ipsa quae ab illo inventore veritatis et quasi architecto beatae vitae dicta sunt explicabo. Nemo enim ipsam voluptatem quia voluptas sit aspernatur aut odit aut fugit, sed quia consequuntur magni dolores eos qui ratione voluptatem sequi nesciunt. Neque porro quisquam est, qui dolorem ipsum quia dolor sit amet, consectetur, adipisci velit, sed quia non numquam eius modi tempora incidunt ut labore et dolore magnam aliquam quaerat voluptatem.</p>
<div class="abs welcome-photo" role="img" aria-label="Photo of a leather tool belt with hammer and pliers beside a red hard hat"></div>
<div class="abs divider"></div>

<h2 class="abs section-title services-title">Our Services</h2>
<div class="abs services-rule"></div>
<p class="abs body-copy services-intro">Nemo enim ipsam voluptatem quia voluptas sit aspernatur aut odit aut fugit, sed quia consequuntur magni dolores eos qui ratione voluptatem sequi nesciunt. Neque porro quisquam est, qui dolorem ipsum quia dolor sit amet.</p>

<div class="abs service-thumb thumb-tools" role="img" aria-label="Photo of a hammer, nails and square on timber boards"></div>
<p class="abs body-copy service-copy" style="top:783px">At vero eos et accusamus et iusto odio dignissimos ducimus qui blanditiis praesentium voluptatum deleniti atque corrupti quos dolores et quas molestias excepturi sint occaecati cupiditate non provident, similique sunt in culpa qui officia deserunt mollitia animi, id est laborum et dolorum fuga.<br><a href="#">View more</a></p>

<div class="abs service-thumb thumb-electric" role="img" aria-label="Photo of a tradesman fitting a ceiling light in a bright room"></div>
<p class="abs body-copy service-copy" style="top:920px">At vero eos et accusamus et iusto odio dignissimos ducimus qui blanditiis praesentium voluptatum deleniti atque corrupti quos dolores et quas molestias excepturi sint occaecati cupiditate non provident, similique sunt in culpa qui officia deserunt mollitia animi, id est laborum et dolorum fuga.<br><a href="#">View more</a></p>

<h2 class="abs section-title other-title">Other Services</h2>
<div class="abs other-panel"></div>
<ul class="abs other-list">
  <li><svg width="6" height="9"><path d="M0 0L6 4.5 0 9z" fill="#777"/></svg>Phasellus pharetra</li>
  <li><svg width="6" height="9"><path d="M0 0L6 4.5 0 9z" fill="#777"/></svg>Aenean ullamcorper</li>
  <li><svg width="6" height="9"><path d="M0 0L6 4.5 0 9z" fill="#777"/></svg>Aliquam molestie</li>
  <li><svg width="6" height="9"><path d="M0 0L6 4.5 0 9z" fill="#777"/></svg>Maecenas suscipit odio</li>
  <li><svg width="6" height="9"><path d="M0 0L6 4.5 0 9z" fill="#777"/></svg>Suspendisse non ante</li>
  <li><svg width="6" height="9"><path d="M0 0L6 4.5 0 9z" fill="#777"/></svg>Fusce mentum volutpat</li>
  <li><svg width="6" height="9"><path d="M0 0L6 4.5 0 9z" fill="#777"/></svg>Aenean velnisi</li>
  <li><svg width="6" height="9"><path d="M0 0L6 4.5 0 9z" fill="#777"/></svg>Pellentesque anulla</li>
</ul>

<footer class="abs site-footer"></footer>
<nav class="abs footer-nav">
  <a href="#">Home</a><span class="bar">|</span><a href="#">About Us</a><span class="bar">|</span><a href="#">Residential</a><span class="bar">|</span><a href="#">Commercial</a><span class="bar">|</span><a href="#">Real Estate/Strata</a><span class="bar">|</span><a href="#">Contact Us/Quote</a><span class="bar">|</span><a href="#">Blog</a>
</nav>
<div class="abs copyright">Copyright © 2102 www.tallridgemaint.com.au<span>All rights reserved.</span></div>
<div class="abs social" aria-label="Social links"><span></span><span></span></div>
</body>
</html>
```